Submittal Letter - Letterhead

want something that matches our colors that looks professional for a design build engineering fan. Feel Free to incorporate Engineering, Procurement, Construction and Maintenance as a tagline type heading if it makes sense.

```html
<!DOCTYPE html>
<html lang="en">
<head>
<meta charset="utf-8">
<title>Dalton Rhodes – Letterhead</title>
<link href="https://fonts.googleapis.com/css2?family=Lato:wght@400;700&family=Montserrat:wght@400;500&family=Tangerine:wght@700&display=swap" rel="stylesheet">
<style>
  :root {
    --backdrop: #e4e4e4;
    --paper: #ffffff;
    --ink: #141414;
    --ink-soft: #2b2b2b;
    --brand-red: #c8252c;
    --brand-gold: #e2a822;
    --brand-black: #111111;
  }
  * { margin: 0; padding: 0; box-sizing: border-box; }
  html, body {
    width: 1200px; height: 1079px; overflow: hidden;
    background: var(--backdrop);
  }
  .letterhead {
    position: absolute; left: 233px; top: 21px;
    width: 733px; height: 1037px;
    background: var(--paper);
    font-family: 'Lato', sans-serif;
    color: var(--ink);
  }
  .brand {
    position: absolute; left: 37px; top: 86px;
    display: flex; align-items: center; gap: 10px;
  }
  .brand-dot {
    width: 34px; height: 34px; border-radius: 50%;
    background: var(--brand-red);
  }
  .brand-name {
    font-family: 'Lato', sans-serif; font-weight: 700;
    font-size: 27px; color: var(--brand-black); letter-spacing: 0.2px;
  }
  .contact-rule {
    position: absolute; left: 469px; top: 56px;
    width: 1.5px; height: 98px; background: var(--brand-red);
  }
  .contact {
    position: absolute; left: 499px; top: 52px;
    font-family: 'Montserrat', sans-serif; font-size: 12.8px;
    line-height: 18px; color: var(--ink-soft);
  }
  .contact-lines { margin-bottom: 14px; }
  .contact-item { display: flex; align-items: center; gap: 5px; margin-left: 0; }
  .contact-item svg { width: 12px; height: 12px; flex: none; }
  .letter {
    position: absolute; left: 37px; width: 659px;
    font-size: 14.6px; line-height: 16.3px;
  }
  .letter-date { top: 295px; }
  .letter-recipient { top: 331px; }
  .letter-company { top: 382px; }
  .letter-salutation { top: 454px; font-size: 19px; font-weight: 700; line-height: 22px; }
  .letter-body { top: 495px; text-align: justify; }
  .letter-body p { margin-bottom: 16px; }
  .letter-closing { top: 791px; }
  .letter-signature {
    top: 858px; font-family: 'Tangerine', cursive;
    font-size: 40px; line-height: 44px; font-weight: 700;
  }
  .footer-band {
    position: absolute; left: 0; right: 0; top: 993px;
  }
  .footer-black { height: 2.5px; background: var(--brand-black); }
  .footer-gap { height: 2.5px; }
  .footer-red {
    height: 18px; background: var(--brand-red);
    color: #fff; font-family: 'Montserrat', sans-serif;
    font-size: 14.3px; line-height: 18px; padding-left: 37px;
    letter-spacing: 0.15px; white-space: nowrap;
  }
  .footer-gold { height: 2.5px; margin-top: 2px; background: var(--brand-gold); }
</style>
</head>
<body>
  <main class="letterhead">
    <header>
      <div class="brand">
        <span class="brand-dot"></span>
        <span class="brand-name">Dalton Rhodes</span>
      </div>
      <div class="contact-rule"></div>
      <address class="contact" style="font-style:normal">
        <div class="contact-lines">
          Dalton Rhodes, Inc. (DRI)<br>
          4170 Harborview Avenue<br>
          Fairmont, CA 90318
        </div>
        <div class="contact-item">
          <svg viewBox="0 0 24 24" aria-hidden="true"><path fill="#c8252c" d="M6.6 10.8a15.1 15.1 0 0 0 6.6 6.6l2.2-2.2a1 1 0 0 1 1-.25 11.4 11.4 0 0 0 3.6.57 1 1 0 0 1 1 1V20a1 1 0 0 1-1 1A17 17 0 0 1 3 4a1 1 0 0 1 1-1h3.5a1 1 0 0 1 1 1c0 1.25.2 2.45.57 3.57a1 1 0 0 1-.25 1z"/></svg>
          (800) 555-0148
        </div>
        <div class="contact-item">
          <svg viewBox="0 0 24 24" aria-hidden="true"><circle cx="12" cy="12" r="10" fill="#c8252c"/><path d="M2 12h20M12 2c3 3 3 17 0 20M12 2c-3 3-3 17 0 20" stroke="#fff" stroke-width="1.4" fill="none"/></svg>
          www.drinc.com
        </div>
      </address>
    </header>

    <div class="letter letter-date">January-03-2020</div>
    <div class="letter letter-recipient">Mr, John Doe<br>President</div>
    <div class="letter letter-company">Link Corpporation<br>123 Street Name, Suite# 10<br>City, State, 120023</div>
    <div class="letter letter-salutation">Dear Mr, John</div>
    <div class="letter letter-body">
      <p>Lorem ipsum dolor sit amet, consectetur adipiscing elit, sed do eiusmod tempor incididunt ut labore et dolore magna aliqua. Ut enim ad minim veniam, quis nostrud exercitation ullamco laboris nisi ut aliquip ex ea commodo consequat. Duis aute irure dolor in reprehenderit in voluptate velit esse cillum dolore eu fugiat nulla pariatur.</p>
      <p>Lorem ipsum dolor sit amet, consectetur adipiscing elit, sed do eiusmod tempor incididunt ut labore et dolore magna aliqua. Ut enim ad minim veniam, quis nostrud exercitation ullamco laboris nisi ut aliquip ex ea commodo consequat. Duis aute irure dolor in reprehenderit in voluptate velit esse cillum dolore eu fugiat nulla pariatur.</p>
      <p>Lorem ipsum dolor sit amet, consectetur adipiscing elit, sed do eiusmod tempor incididunt ut labore et dolore magna aliqua. Ut enim ad minim veniam, quis nostrud exercitation ullamco laboris nisi ut aliquip ex ea commodo consequat.</p>
      <p>Excepteur sint occaecat cupidatat non proident, sunt in culpa qui officia deserunt mollit anim id est laborum. re et dolore magnam aliquam quaerat voluptatem.</p>
    </div>
    <div class="letter letter-closing">Regards</div>
    <div class="letter letter-signature">Michel Smith</div>

    <footer class="footer-band">
      <div class="footer-black"></div>
      <div class="footer-gap"></div>
      <div class="footer-red">Feel Free to incorporate Engineering, Procurement, Construction and Maintenance</div>
      <div class="footer-gold"></div>
    </footer>
  </main>
</body>
</html>
```